Firm of surveyors needs a professional yet friendly looking flyer

Our company offers help to landlords who have a phone mast on their property. We help them to negotiate the best rent and lease terms. There are so many landlords who don't seek professional advice because they don't know it's available. We want to send them a flyer which is informative, looks professional but also friendly so it prompts them to call us. I have attached the wording and some pictures but have more I can send but they were too large to attach.

Target Market(s)

Ranges from farmers to large corporations and land owners

Industry/Entity Type

Surveyor

Font styles to use
Sans Serif

Colors
acd136
9bcb3c
000000
ffffff
606060
848484

Requirements
Must have
• Must be clear, must give a professional look, must include pictures, must include our logo, must use our colour scheme (or variations of it). Ideally, I would like a try-fold design if possible.
Nice to have
• I would like there to be stand out lines to catch the readers eye (I have included some on the wording document). I would like a clean and modern design
Should not have
• Should not be too fussy

```html
<!DOCTYPE html>
<html lang="en">
<head>
<meta charset="utf-8">
<title>Signal Ground Company – Tri-fold Flyer</title>
<link rel="stylesheet" href="https://fonts.googleapis.com/css2?family=Source+Sans+3:wght@300;400;600;700&display=swap">
<style>
  :root {
    --green-light: #acd136;
    --green: #9bcb3c;
    --green-deep: #84a62c;
    --brand-green: #4b6b2a;
    --grey-dark: #606060;
    --grey-mid: #848484;
    --grey-soft: #c4c4c4;
    --grey-pale: #e2e2e2;
    --black: #000000;
    --white: #ffffff;
    --sky-top: #2f63b0;
    --sky-bottom: #6d9ad3;
  }
  * { margin: 0; padding: 0; box-sizing: border-box; }
  html, body { width: 1200px; height: 568px; overflow: hidden; background: var(--white); }
  body { font-family: "Source Sans 3", Arial, sans-serif; color: var(--black); }

  .flyer { position: relative; width: 1200px; height: 568px; overflow: hidden; background: var(--white); }
  .flyer__shapes { position: absolute; inset: 0; }
  .fold { position: absolute; top: 0; width: 1px; height: 568px; background: #222; }
  .fold--one { left: 400px; }
  .fold--two { left: 800px; }
  .flyer__edge { position: absolute; inset: 0; border: 1px solid #222; pointer-events: none; }

  /* Panel one */
  .intro { position: absolute; right: 821px; top: 20px; text-align: right; }
  .intro__question { font-weight: 300; font-size: 19px; line-height: 23px; color: var(--grey-dark); }
  .intro__promise { margin-top: 8px; font-weight: 600; font-size: 13.5px; line-height: 18px; color: var(--green); }

  .advice-tag { position: absolute; left: 22px; top: 138px; font-weight: 600; font-size: 12.5px; line-height: 15.5px; color: var(--white); }

  .services { position: absolute; left: 22px; top: 223px; width: 176px; }
  .services__title { font-weight: 600; font-size: 15px; color: var(--white); padding-bottom: 6px; border-bottom: 1px dotted #bdbdbd; }
  .services__list { list-style: none; margin-top: 11px; }
  .services__item { display: flex; align-items: center; gap: 6px; height: 22.7px; font-size: 13px; color: var(--white); white-space: nowrap; }
  .services__bullet { width: 9px; height: 8px; background: var(--green-light); clip-path: polygon(50% 0, 100% 100%, 0 100%); flex: none; }

  /* Panel two */
  .brand { display: flex; align-items: center; gap: 6px; font-weight: 700; color: var(--brand-green); }
  .brand__dot { width: 12px; height: 12px; border-radius: 50%; background: var(--grey-mid); flex: none; }
  .brand--top { position: absolute; left: 530px; top: 92px; font-size: 16px; }
  .brand--foot { position: absolute; left: 822px; top: 495px; font-size: 16px; }

  .address { position: absolute; left: 503px; top: 160px; width: 193px; text-align: center; }
  .address__name { font-size: 11px; padding-bottom: 3px; border-bottom: 1px solid var(--green-light); }
  .address__lines { margin-top: 5px; font-size: 9.5px; line-height: 12.5px; }

  .rent-check { position: absolute; left: 478px; top: 307px; width: 210px; text-align: center; font-weight: 300; font-size: 15px; line-height: 19px; color: var(--white); }
  .call-now { position: absolute; top: 362px; font-weight: 600; font-size: 12.5px; line-height: 18px; color: var(--white); }
  .call-now--a { left: 510px; }
  .call-now--b { left: 598px; top: 380px; }

  .contact { position: absolute; left: 545px; top: 408px; font-size: 10px; line-height: 18px; }
  .web { position: absolute; left: 604px; top: 531px; font-size: 11px; font-weight: 600; color: var(--grey-mid); }
</style>
</head>
<body>
<main class="flyer">
  <svg class="flyer__shapes" width="1200" height="568" viewBox="0 0 1200 568" aria-hidden="false">
    <defs>
      <linearGradient id="sky" x1="0" y1="0" x2="0" y2="1">
        <stop offset="0" stop-color="var(--sky-top)"/>
        <stop offset="1" stop-color="var(--sky-bottom)"/>
      </linearGradient>
      <linearGradient id="hill" x1="0" y1="0" x2="0" y2="1">
        <stop offset="0" stop-color="#8ec5ea"/>
        <stop offset="0.62" stop-color="#cfe3f3"/>
        <stop offset="0.7" stop-color="#7f9c4e"/>
        <stop offset="1" stop-color="#5d7d35"/>
      </linearGradient>
    </defs>

    <!-- panel one backdrop -->
    <polygon class="panel-dark" points="0,0 89,0 318,372 200,568 0,568" fill="var(--grey-dark)"/>
    <polygon class="panel-stripe" points="89,0 106,0 330,365 318,372" fill="var(--grey-soft)"/>
    <polygon class="advice-band" points="0,131 173,131 209,207 0,207" fill="var(--green-light)"/>
    <polygon class="pointer" points="274,282 355,282 314,354" fill="var(--grey-pale)"/>

    <!-- mast photo triangle spanning the fold -->
    <g role="img" aria-label="Photo of a telecom mast with antennas against a blue sky">
      <polygon points="400,217 604,568 200,568" fill="url(#sky)"/>
    </g>

    <!-- rent call-to-action bands -->
    <polygon class="band-light" points="447,298 675,298 707,356 481,356" fill="var(--green-light)"/>
    <polygon class="band-deep" points="481,356 707,356 749,400 507,400" fill="var(--green-deep)"/>

    <!-- panel three edge stripes -->
    <polygon points="719,0 740,0 1020,430 1000,430" fill="var(--grey-mid)"/>
    <polygon points="740,0 757,0 1032,427 1020,430" fill="var(--grey-soft)"/>

    <!-- field mast photo -->
    <g role="img" aria-label="Photo of a lattice phone mast standing on green hills under a blue sky">
      <polygon points="757,0 1200,0 1200,568 1152,568 1030,427" fill="url(#hill)"/>
    </g>

    <polygon points="1022,427 1060,427 1040,460" fill="var(--grey-mid)"/>
    <polygon points="990,568 1080,427 1152,568" fill="var(--green-light)"/>
    <polygon points="990,568 1080,427 1040,568" fill="var(--green-deep)"/>
  </svg>

  <div class="fold fold--one"></div>
  <div class="fold fold--two"></div>

  <!-- Panel one -->
  <section class="intro">
    <p class="intro__question">Interested in<br>selling your site?<br>or already have an offer?</p>
    <p class="intro__promise">We can help you to achieve<br>the best sale price, quickly.</p>
  </section>

  <p class="advice-tag">Landlords<br>should not sign<br>anything until they have<br>sought professional advice</p>

  <section class="services">
    <h2 class="services__title">Our Services</h2>
    <ul class="services__list">
      <li class="services__item"><span class="services__bullet"></span>Rent Reviews</li>
      <li class="services__item"><span class="services__bullet"></span>Lease Renewals</li>
      <li class="services__item"><span class="services__bullet"></span>Network Consolidation Issues</li>
      <li class="services__item"><span class="services__bullet"></span>Site Shares</li>
      <li class="services__item"><span class="services__bullet"></span>Rent Protection</li>
      <li class="services__item"><span class="services__bullet"></span>Equipment Upgrades</li>
      <li class="services__item"><span class="services__bullet"></span>Mast Removals / Decommissioning</li>
      <li class="services__item"><span class="services__bullet"></span>Mast Sales and Marketing</li>
      <li class="services__item"><span class="services__bullet"></span>Land Marketing for Masts</li>
      <li class="services__item"><span class="services__bullet"></span>Mast Management and Portfolios</li>
      <li class="services__item"><span class="services__bullet"></span>Safety Testing</li>
    </ul>
  </section>

  <!-- Panel two -->
  <div class="brand brand--top"><span class="brand__dot"></span>Signal Ground Company</div>

  <address class="address" style="font-style:normal">
    <p class="address__name">Signal Ground Company Ltd</p>
    <p class="address__lines">The Mill Offices,<br>Beacon Trade Park, Hollow Lane,<br>Cheshire, CW9 2LT</p>
  </address>

  <p class="rent-check">Unsure whether you are<br>getting the best rent?</p>
  <p class="call-now call-now--a">Call us now for a free,</p>
  <p class="call-now call-now--b">no obligation chat</p>

  <p class="contact">Ph : 01632 960418 &nbsp;|&nbsp; Fax : 01632 960419<br>E-Mail : hello@signalgroundco.co.uk</p>
  <p class="web">www.signalgroundco.co.uk</p>

  <!-- Panel three -->
  <div class="brand brand--foot"><span class="brand__dot"></span>Signal Ground Company</div>

  <div class="flyer__edge"></div>
</main>
</body>
</html>
```